Need a Facebook image for childcare advertisement

We are after a design for Facebook advertisement for childcare and kindergarten centre enrolments for 2023.

I have attached a previous flyer that we have in pdf format. The new logo is also attached with this brief.

All other information is still current as per the attached flyer.

You can use same colours as per attached flyer. I will also attached some stock images that you can select to use for the design.

our website for your reference:

https://tolvenbrook.com.au

```html
<!DOCTYPE html>
<html lang="en">
<head>
<meta charset="utf-8">
<title>Tolvenbrook – Enrol Now</title>
<link href="https://fonts.googleapis.com/css2?family=Open+Sans:wght@800&family=Poppins:wght@600;700&family=Roboto+Condensed:wght@400&display=swap" rel="stylesheet">
<style>
  :root {
    --green: #7ab843;
    --dark-green: #0d8a3c;
    --yellow: #ffe200;
    --white: #ffffff;
    --ink: #222222;
    --phone-blue: #4aa3df;
  }
  html, body {
    margin: 0;
    width: 1200px;
    height: 1200px;
    overflow: hidden;
    background: var(--white);
  }
  .ad {
    position: relative;
    width: 1200px;
    height: 1200px;
    background: var(--white);
    font-family: "Poppins", sans-serif;
  }
  .ad__shapes {
    position: absolute;
    inset: 0;
  }
  .headline {
    position: absolute;
    left: 0;
    top: 772px;
    width: 526px;
    margin: 0;
    text-align: center;
    font-family: "Open Sans", sans-serif;
    font-weight: 800;
    font-size: 50px;
    line-height: 62px;
    color: var(--white);
    text-transform: uppercase;
    letter-spacing: -0.5px;
  }
  .enrol-button {
    position: absolute;
    left: 140px;
    top: 1007px;
    width: 230px;
    height: 96px;
    display: flex;
    align-items: center;
    gap: 20px;
    color: var(--dark-green);
    font-weight: 700;
    font-size: 46px;
    line-height: 45px;
    text-decoration: none;
  }
  .enrol-button__label { display: block; text-align: center; }
  .website {
    position: absolute;
    left: 0;
    top: 1126px;
    width: 506px;
    text-align: center;
    font-weight: 700;
    font-size: 31px;
    color: var(--yellow);
  }
  .brand {
    position: absolute;
    left: 640px;
    top: 860px;
    width: 460px;
    text-align: center;
  }
  .brand__name {
    margin: 0;
    font-weight: 700;
    font-size: 60px;
    line-height: 72px;
    color: var(--ink);
  }
  .brand__tagline {
    margin: 10px 0 0;
    font-family: "Roboto Condensed", sans-serif;
    font-weight: 400;
    font-size: 25px;
    line-height: 30px;
    color: var(--ink);
    text-transform: uppercase;
    letter-spacing: 0.3px;
  }
  .info-box {
    position: absolute;
    left: 644px;
    top: 1024px;
    width: 447px;
    height: 132px;
    border: 1.5px solid var(--green);
    border-radius: 14px;
    box-sizing: border-box;
    text-align: center;
    padding-top: 10px;
  }
  .info-box__title {
    font-weight: 700;
    font-size: 42px;
    line-height: 54px;
    color: var(--dark-green);
  }
  .info-box__phone {
    display: flex;
    justify-content: center;
    align-items: center;
    gap: 12px;
    font-weight: 700;
    font-size: 42px;
    line-height: 56px;
    color: var(--phone-blue);
  }
</style>
</head>
<body>
<main class="ad">
  <svg class="ad__shapes" width="1200" height="1200" viewBox="0 0 1200 1200">
    <defs>
      <linearGradient id="mainPhotoTone" x1="0" y1="0" x2="0" y2="1">
        <stop offset="0" stop-color="#f4efea"/>
        <stop offset="0.35" stop-color="#e8cdbd"/>
        <stop offset="0.7" stop-color="#d9a08c"/>
        <stop offset="1" stop-color="#e0646a"/>
      </linearGradient>
      <linearGradient id="classPhotoTone" x1="0" y1="0" x2="1" y2="1">
        <stop offset="0" stop-color="#f0dcd0"/>
        <stop offset="1" stop-color="#d9a0a0"/>
      </linearGradient>
      <linearGradient id="readingPhotoTone" x1="0" y1="0" x2="1" y2="1">
        <stop offset="0" stop-color="#f1e2da"/>
        <stop offset="1" stop-color="#c9e3df"/>
      </linearGradient>
    </defs>

    <!-- top yellow swoosh -->
    <path class="accent-swoosh" d="M 262 88 C 320 40 380 12 430 0 L 475 0 C 410 20 340 60 290 105 Z" fill="var(--yellow)"/>

    <!-- main photo with yellow rim -->
    <path class="main-photo__rim" d="M 430 0 L 1200 0 L 1200 608 C 1150 715 1050 770 935 766 C 810 762 690 712 570 640 L 540 460 C 470 320 430 150 430 0 Z" fill="var(--yellow)"/>
    <path class="main-photo" role="img" aria-label="Photo of a teacher sitting on a red classroom rug playing with young children"
          d="M 440 0 L 1200 0 L 1200 595 C 1155 700 1055 752 935 749 C 815 746 700 700 585 630 L 550 455 C 480 320 440 150 440 0 Z" fill="url(#mainPhotoTone)"/>

    <!-- small photo: class drawing -->
    <path class="inset-photo" role="img" aria-label="Photo of young children drawing at a classroom table"
          d="M 160 75 C 210 55 340 70 440 120 C 490 145 495 195 465 240 C 410 310 340 370 300 400 C 260 428 230 420 210 390 C 170 320 130 220 125 160 C 122 115 135 88 160 75 Z"
          fill="url(#classPhotoTone)" stroke="var(--yellow)" stroke-width="5"/>

    <!-- small photo: reading together -->
    <path class="inset-photo" role="img" aria-label="Photo of a teacher reading a book with two young girls"
          d="M 440 380 C 480 360 530 370 555 420 C 585 480 592 560 570 600 C 548 630 490 630 420 620 C 350 610 315 585 330 545 C 350 490 395 405 440 380 Z"
          fill="url(#readingPhotoTone)" stroke="var(--yellow)" stroke-width="5"/>

    <!-- green message panel with yellow edge -->
    <path class="panel__edge" d="M 0 568 C 30 640 80 668 170 640 C 300 605 480 615 560 670 C 640 725 630 830 615 900 C 590 1010 570 1110 580 1200 L 0 1200 Z" fill="var(--yellow)"/>
    <path class="panel" d="M 0 580 C 35 655 95 690 200 672 C 330 650 490 655 560 705 C 615 745 605 815 590 870 C 555 990 535 1100 545 1200 L 0 1200 Z" fill="var(--green)"/>

    <!-- spark marks above headline -->
    <g class="spark" stroke="var(--white)" stroke-width="4" stroke-linecap="round">
      <line x1="232" y1="740" x2="243" y2="766"/>
      <line x1="256" y1="736" x2="256" y2="766"/>
      <line x1="281" y1="740" x2="270" y2="766"/>
    </g>

    <!-- enrol button shape -->
    <path class="enrol-button__bg" d="M 125 998 C 200 985 320 980 362 990 C 392 997 412 1055 396 1085 C 382 1103 300 1108 200 1106 C 128 1104 100 1090 108 1050 C 113 1020 115 1002 125 998 Z" fill="var(--yellow)"/>
  </svg>

  <h1 class="headline">Spark a lifelong<br>love of learning<br>in your child</h1>

  <a class="enrol-button" href="https://tolvenbrook.com.au">
    <svg width="46" height="46" viewBox="0 0 46 46" aria-hidden="true">
      <circle cx="23" cy="23" r="20" fill="none" stroke="var(--dark-green)" stroke-width="3"/>
      <path d="M 18 13 L 29 23 L 18 33" fill="none" stroke="var(--dark-green)" stroke-width="4" stroke-linecap="round" stroke-linejoin="round"/>
    </svg>
    <span class="enrol-button__label">Enrol<br>Now</span>
  </a>

  <div class="website">www.tolvenbrook.com.au</div>

  <div class="brand">
    <p class="brand__name">Tolvenbrook</p>
    <p class="brand__tagline">Early Childhood Learning Centre</p>
  </div>

  <div class="info-box">
    <div class="info-box__title">More Information</div>
    <div class="info-box__phone">
      <svg width="40" height="40" viewBox="0 0 40 40" aria-hidden="true">
        <circle cx="20" cy="20" r="17" fill="none" stroke="var(--phone-blue)" stroke-width="3"/>
        <path d="M 13 11 C 11 13 11 17 14 22 C 17 27 22 30 26 29 L 28 26 L 24 23 L 22 25 C 19 24 16 21 15 18 L 17 16 L 15 11 Z" fill="var(--phone-blue)"/>
      </svg>
      <span>(03) 9000 4127</span>
    </div>
  </div>
</main>
</body>
</html>
```